I need the Scorecard I've developed for my staff to be produced into a visually engaging piece that will encourage the staff to utilize it on a daily basis. I'm thinking it could be 5x7 in size so that it isn't too cumbersome, but I'm open to different layouts.
I have multiple other departments that will need Scorecards created for them as well, but each one will contain task specific questions for each department.

```html
<!DOCTYPE html>
<html lang="en">
<head>
<meta charset="utf-8">
<title>Receptionist Daily Excellence Scorecard</title>
<link href="https://fonts.googleapis.com/css2?family=Poppins:wght@400;500;600;700&display=swap" rel="stylesheet">
<style>
:root{
  --backdrop:#959595;
  --paper:#ffffff;
  --navy:#333a64;
  --navy-table:#2f3873;
  --orange:#c47a45;
  --orange-light:#d49061;
  --ink:#1f2333;
  --line:#cfd2dc;
  --heading:#262b55;
}
*{margin:0;padding:0;box-sizing:border-box}
html,body{width:1200px;height:878px;overflow:hidden;background:var(--backdrop);font-family:'Poppins',sans-serif;color:var(--ink)}
.page{position:absolute;top:62px;width:508px;height:711px;background:var(--paper);overflow:hidden}
.page-one{left:76px}
.page-two{left:617px}
.abs{position:absolute}
.header-band{left:0;top:0;width:508px;height:129px;background:var(--navy)}
.title-tab{left:0;top:0;width:508px;height:52px}
.title{left:0;top:18px;width:508px;text-align:center;color:#fff;font-weight:700;font-size:16px;letter-spacing:.1px}
.label{background:var(--orange);color:#fff;font-size:8.5px;line-height:15px;padding-left:4px;height:15px}
.field{background:#fff;height:15px}
.instruction{left:41px;top:123px;width:430px;height:17px;border:1px solid var(--line);background:#fff;font-size:8.6px;line-height:15px;padding-left:8px}
.section{position:absolute;left:41px;width:430px}
.section-head{display:flex;align-items:center;gap:10px;height:18px;margin-bottom:7px;margin-left:0}
.num{width:18px;height:18px;border-radius:50%;background:var(--orange);color:#fff;font-size:10px;font-weight:600;display:flex;align-items:center;justify-content:center}
.section-title{font-size:11.5px;font-weight:600;color:var(--ink);text-transform:uppercase}
table{width:430px;border-collapse:collapse}
th{background:var(--navy-table);color:#fff;font-weight:400;font-size:8.5px;height:14px;border:1px solid var(--navy-table)}
th.task{width:168px}
td{border:1px solid var(--line);font-size:7px;height:15px;padding-left:8px}
td.note{padding:0}
.blue-head{font-size:11.5px;font-weight:600;color:var(--heading);text-transform:uppercase}
.status{left:41px;top:277px;width:430px}
.status-row{display:flex;height:14.5px;border:1px solid var(--line);border-top:none}
.status-row:first-child{border-top:1px solid var(--line)}
.status-tag{width:88px;background:var(--orange);color:#fff;font-size:8.3px;font-weight:600;display:flex;align-items:center;gap:6px;padding-left:5px}
.status-tag::before{content:"";width:4px;height:4px;border-radius:50%;background:#fff}
.status-text{font-size:8.3px;padding-left:10px;display:flex;align-items:center}
.prompt{left:39px;font-size:9.5px;font-weight:500}
.box{left:39px;width:434px;height:15px;border:1px solid var(--line)}
.small{left:39px;font-size:8.3px;font-weight:500}
.sig{top:664px;width:122px;border-top:1px solid var(--line);padding-top:5px;font-size:7.6px;font-weight:600}
</style>
</head>
<body>

<section class="page page-one">
  <div class="abs header-band"></div>
  <svg class="abs title-tab" viewBox="0 0 508 52" aria-hidden="true">
    <defs><linearGradient id="tabFill" x1="0" x2="1"><stop offset="0" stop-color="#c27442"/><stop offset="1" stop-color="#d1915f"/></linearGradient></defs>
    <path d="M24 0 H476 C468 14 462 40 448 48 Q444 52 436 52 H64 Q56 52 52 48 C38 40 32 14 24 0Z" fill="url(#tabFill)"/>
  </svg>
  <h1 class="abs title">RECEPTIONIST DAILY EXCELLENCE SCORECARD</h1>

  <div class="abs label" style="left:41px;top:69px;width:36px">Name</div>
  <div class="abs field" style="left:77px;top:69px;width:237px"></div>
  <div class="abs label" style="left:324px;top:69px;width:36px">Date</div>
  <div class="abs field" style="left:360px;top:69px;width:111px"></div>
  <div class="abs label" style="left:41px;top:90px;width:42px">Location</div>
  <div class="abs field" style="left:83px;top:90px;width:388px"></div>

  <div class="abs instruction">(Please rate yourself for each task: 1 = Needs Improvement, 3 = Meets Expectations, 5 =Excellent)</div>

  <div class="section" style="top:177px">
    <div class="section-head"><span class="num">1</span><h2 class="section-title">Call Handling &amp; First Call Intake</h2></div>
    <table><tr><th class="task">Task</th><th>Self-Rating (1-5) Notes / Issues</th></tr>
      <tr><td>Answered 90%+ calls within 3 rings</td><td class="note"></td></tr>
      <tr><td>Maintained empathy and professionalism</td><td class="note"></td></tr>
      <tr><td>Accurately completed all First Call fields</td><td class="note"></td></tr>
      <tr><td>Worked within Receptionist role</td><td class="note"></td></tr>
    </table>
  </div>

  <div class="section" style="top:304px">
    <div class="section-head"><span class="num">2</span><h2 class="section-title">Call Management During Busy Time</h2></div>
    <table><tr><th class="task">Task</th><th>Self-Rating (1-5) Notes / Issues</th></tr>
      <tr><td>Prioritized urgent vs. non-urgent calls</td><td class="note"></td></tr>
      <tr><td>Hold times under 1 minute</td><td class="note"></td></tr>
      <tr><td>Logged all calls</td><td class="note"></td></tr>
      <tr><td>Requested help if overwhelmed</td><td class="note"></td></tr>
    </table>
  </div>

  <div class="section" style="top:433px">
    <div class="section-head"><span class="num">3</span><h2 class="section-title">Scheduling Accuracy</h2></div>
    <table><tr><th class="task">Task</th><th>Self-Rating (1-5) Notes / Issues</th></tr>
      <tr><td>Updated scheduling board</td><td class="note"></td></tr>
      <tr><td>Cross-checked with Red Book</td><td class="note"></td></tr>
      <tr><td>Entered manifold info promptly</td><td class="note"></td></tr>
    </table>
  </div>

  <div class="section" style="top:546px">
    <div class="section-head"><span class="num">4</span><h2 class="section-title">Clothing &amp; Flowers</h2></div>
    <table><tr><th class="task">Task</th><th>Self-Rating (1-5) Notes / Issues</th></tr>
      <tr><td>Clothing sheet completed</td><td class="note"></td></tr>
      <tr><td>Family contact noted on sheet</td><td class="note"></td></tr>
      <tr><td>Floral deliveries logged</td><td class="note"></td></tr>
      <tr><td>Concerns communicated to Care Center</td><td class="note"></td></tr>
      <tr><td>Flower placement verified</td><td class="note"></td></tr>
    </table>
  </div>
</section>

<section class="page page-two">
  <div class="section" style="top:29px">
    <div class="section-head"><span class="num">6</span><h2 class="section-title">Death Certificates</h2></div>
    <table><tr><th class="task">Task</th><th>Self-Rating (1-5) Notes / Issues</th></tr>
      <tr><td>Verified recipient ID &amp; relationship</td><td class="note"></td></tr>
      <tr><td>Confirmed correct documents enclosed</td><td class="note"></td></tr>
      <tr><td>Recipient signed the DC logbook</td><td class="note"></td></tr>
      <tr><td>Suggested proofreading before leaving</td><td class="note"></td></tr>
    </table>
  </div>

  <div class="section" style="top:149px">
    <div class="section-head"><span class="num">7</span><h2 class="section-title">Routing &amp; Messages</h2></div>
    <table><tr><th class="task">Task</th><th>Self-Rating (1-5) Notes / Issues</th></tr>
      <tr><td>Calls routed appropriately</td><td class="note"></td></tr>
      <tr><td>Messages included all required info</td><td class="note"></td></tr>
      <tr><td>Delivered 95%+ messages in 30 min</td><td class="note"></td></tr>
    </table>
  </div>

  <h2 class="abs blue-head" style="left:40px;top:253px">Daily Status Summary (Circle One)</h2>
  <div class="abs status">
    <div class="status-row"><span class="status-tag">Excellent</span><span class="status-text">All key duties completed, proactive, calm under pressure</span></div>
    <div class="status-row"><span class="status-tag">Satisfactory</span><span class="status-text">Most duties completed, minor follow-up needed</span></div>
    <div class="status-row"><span class="status-tag">Needs Support</span><span class="status-text">Missed urgent duties, accuracy or stress issues</span></div>
  </div>

  <h2 class="abs blue-head" style="left:39px;top:333px">Daily Reflection</h2>
  <p class="abs prompt" style="top:351px">What went well today?</p>
  <div class="abs box" style="top:367px"></div>
  <p class="abs prompt" style="top:386px">Any issues or barriers to note?</p>
  <div class="abs box" style="top:403px"></div>
  <p class="abs prompt" style="top:423px">Support needed from supervisor?</p>
  <div class="abs box" style="top:440px"></div>

  <h2 class="abs blue-head" style="left:39px;top:466px">Stars &amp; Flags (Supervisor Use Only)</h2>
  <p class="abs prompt" style="top:484px">Stars (Excellence or above-and-beyond moments):</p>
  <div class="abs box" style="top:502px"></div>
  <p class="abs prompt" style="top:522px">Flags (Concerns needing follow-up/coaching):</p>
  <div class="abs box" style="top:543px"></div>

  <h2 class="abs blue-head" style="left:39px;top:562px">Manager's Overall Rating</h2>
  <p class="abs prompt" style="top:580px">(Manager: Please rate overall performance on a 1-5 scale)</p>
  <p class="abs small" style="top:596px">Manager Overall Rating (1-5):</p>
  <div class="abs box" style="top:612px"></div>

  <div class="abs sig" style="left:39px">RECEPTIONIST SIGNATURE:</div>
  <div class="abs sig" style="left:194px">SUPERVISOR SIGNATURE:</div>
  <div class="abs sig" style="left:348px">DATE:</div>
</section>

</body>
</html>
```